KV MOTORS BANNER/SIGN DESIGN

Design a banner sign for outdoor use for KV MOTORS - a premium pre owned vehicle sales center. The size must be 36 feet in width
and 3 feet in height.

Information required: logo (attached)
-PREMIUM PRE-OWEND VEHICLE SALES
- 403.555.0172

perhaps in smaller font: BUY-SELL-TRADE

prefer white background but could possibly do red matching the logo

```html
<!DOCTYPE html>
<html lang="en">
<head>
<meta charset="utf-8">
<title>KV Motors Banner</title>
<link href="https://fonts.googleapis.com/css2?family=Montserrat:wght@700&family=Roboto:wght@700;900&display=swap" rel="stylesheet">
<style>
  :root {
    --brand-red: #f0131e;
    --ink: #111111;
    --paper: #ffffff;
    --backdrop: #e9e9e9;
  }
  * { margin: 0; padding: 0; box-sizing: border-box; }
  html, body {
    width: 1200px;
    height: 800px;
    overflow: hidden;
    background: var(--backdrop);
  }
  .stage {
    width: 1200px;
    height: 800px;
    display: flex;
    align-items: center;
    justify-content: center;
  }
  .banner {
    width: 1200px;
    height: 100px;
    background: var(--paper);
    display: flex;
    align-items: center;
    justify-content: space-between;
    padding: 0 34px;
    font-family: "Montserrat", sans-serif;
    color: var(--ink);
  }
  .brand {
    display: flex;
    align-items: center;
    gap: 12px;
    flex: none;
  }
  .brand-mark { width: 54px; height: 54px; display: block; }
  .brand-divider {
    width: 2px;
    height: 52px;
    background: var(--ink);
  }
  .brand-name {
    font-weight: 700;
    font-size: 26px;
    letter-spacing: 1px;
    line-height: 1;
    white-space: nowrap;
  }
  .headline {
    flex: none;
    text-align: center;
    font-weight: 700;
    font-size: 18px;
    line-height: 23px;
    letter-spacing: 0.5px;
    white-space: nowrap;
  }
  .phone {
    flex: none;
    font-family: "Roboto", sans-serif;
    font-weight: 900;
    font-size: 42px;
    line-height: 1;
    letter-spacing: 2px;
    color: var(--brand-red);
    white-space: nowrap;
  }
  .services {
    flex: none;
    border: 2px solid var(--brand-red);
    padding: 4px 5px;
  }
  .services-label {
    background: var(--brand-red);
    color: var(--paper);
    padding: 9px 18px;
    font-family: "Roboto", sans-serif;
    font-weight: 700;
    font-size: 15px;
    line-height: 1;
    white-space: nowrap;
  }
</style>
</head>
<body>
  <div class="stage">
    <main class="banner">
      <header class="brand">
        <svg class="brand-mark" viewBox="0 0 54 54" aria-hidden="true">
          <circle cx="27" cy="27" r="23" fill="none" stroke="var(--brand-red)" stroke-width="4"/>
        </svg>
        <span class="brand-divider"></span>
        <span class="brand-name">KV MOTORS</span>
      </header>

      <h1 class="headline">PREMIUM<br>PRE-OWEND VEHICLE SALES</h1>

      <p class="phone">- 403.555.0172</p>

      <div class="services">
        <div class="services-label">BUY - SELL - TRADE</div>
      </div>
    </main>
  </div>
</body>
</html>
```